1 Page Bio, describing our Mission to buy multifamily properties in Colorado Springs.

I am uploading a sample of an associate who is doing a similar thing in Tampa Florida. I will also upload an attempt by my assistant to make the flyer and I will upload 3 pictures to use, along with another document that has text to add. I want to be able to edit the document pretty easily inside a google doc. thanks, I want it to look clean and professional.

```html
<!DOCTYPE html>
<html lang="en">
<head>
<meta charset="utf-8">
<title>Team Bio – Colorado Springs Multifamily</title>
<link href="https://fonts.googleapis.com/css2?family=Roboto:wght@500;700;900&family=Rubik:wght@400;500;600&display=swap" rel="stylesheet">
<style>
  :root{
    --blue:#1a5590;
    --gold-dark:#d19c18;
    --gold-light:#f8e51b;
    --ink:#1f1f1f;
    --grey-photo:#5a5a5a;
    --grey-soft:#efefef;
    --backdrop:#e8e6e2;
    --paper:#ffffff;
  }
  *{margin:0;padding:0;box-sizing:border-box}
  html,body{width:1200px;height:1200px;overflow:hidden;background:var(--backdrop)}
  body{position:relative;font-family:"Rubik",sans-serif;color:var(--ink)}

  .flyer{
    position:absolute;left:193px;top:30px;
    width:932px;height:1306px;
    background:var(--paper);
    transform:scale(0.873);transform-origin:0 0;
    overflow:hidden;
    box-shadow:0 6px 18px rgba(0,0,0,.18);
  }
  .decor{position:absolute;left:0;top:0;width:932px;height:1306px}

  .column-shade{
    position:absolute;left:470px;top:150px;width:40px;height:930px;
    background:linear-gradient(90deg,rgba(0,0,0,0) 0%,rgba(0,0,0,.05) 100%);
    filter:blur(6px);
  }

  .tag{
    position:absolute;left:0;height:40px;
    padding-left:33px;
    background:linear-gradient(90deg,var(--gold-dark) 0%,var(--gold-light) 100%);
    clip-path:polygon(0 0,calc(100% - 38px) 0,100% 100%,0 100%);
    color:#fff;font-family:"Roboto",sans-serif;font-weight:700;font-size:24px;line-height:40px;
  }
  .body-text{position:absolute;left:34px;font-size:16.5px;line-height:20px}

  .checklist{position:absolute;list-style:none;font-size:16.5px;line-height:20px}
  .checklist li{position:relative;padding-left:23px;margin-bottom:16.5px}
  .checklist li::before{
    content:"";position:absolute;left:2px;top:4px;width:6px;height:11px;
    border:solid var(--blue);border-width:0 2.5px 2.5px 0;transform:rotate(40deg);
  }
  .market-list{left:54px;top:466px;width:400px}
  .principal-list{left:544px;width:380px}

  .contact{position:absolute;left:45px;top:788px}
  .contact-title{font-family:"Roboto",sans-serif;font-weight:700;font-size:24px;color:var(--blue)}
  .contact-title::after{content:"";display:block;width:28px;height:3px;background:var(--blue);margin-top:4px}
  .contact-name{font-size:24px;margin-top:20px}
  .contact-phone{display:flex;align-items:center;gap:10px;margin-top:4px;
    font-family:"Rubik",sans-serif;font-weight:600;font-size:48px;color:var(--blue);letter-spacing:.5px}
  .contact-email{display:flex;align-items:center;gap:10px;margin-top:8px;font-size:24px}

  .team-heading{
    position:absolute;left:508px;top:258px;height:64px;
    border-left:8px solid var(--gold-dark);padding-left:12px;
    font-family:"Roboto",sans-serif;font-weight:700;font-size:46px;line-height:64px;color:var(--blue);
  }
  .principal-name{position:absolute;left:539px;font-family:"Rubik",sans-serif;font-weight:600;font-size:20px;letter-spacing:.3px}
</style>
</head>
<body>
<main class="flyer">
  <svg class="decor" viewBox="0 0 932 1306" aria-hidden="false">
    <defs>
      <linearGradient id="gold" x1="0" y1="0" x2="1" y2="1">
        <stop offset="0" stop-color="#d19c18"/>
        <stop offset="1" stop-color="#f8e51b"/>
      </linearGradient>
      <linearGradient id="goldDiamond" x1="0" y1="0.5" x2="1" y2="0.5">
        <stop offset="0" stop-color="#c99317"/>
        <stop offset="1" stop-color="#f8e51b"/>
      </linearGradient>
    </defs>
    <!-- top band -->
    <polygon points="0,0 549,0 523,26 0,26" fill="var(--blue)"/>
    <!-- team photo -->
    <polygon points="596,88 684,0 932,0 932,178 814,300" fill="#5e6b4e" role="img" aria-label="Photo of the two principals standing outdoors among pine trees"/>
    <!-- gold chevron -->
    <polygon points="549,0 604,0 544,60 728,244 700,272 490,60" fill="url(#gold)"/>

    <!-- bottom left -->
    <polygon points="0,1123 149,998 189,1038 0,1213" fill="var(--blue)"/>
    <polygon points="294,1306 354,1246 404,1268 366,1306" fill="var(--blue)"/>
    <polygon points="253,986 404,1136 253,1287 101,1136" fill="var(--grey-photo)" role="img" aria-label="Black and white portrait of Dean Halvorsen"/>

    <!-- bottom right soft shapes -->
    <polygon points="932,923 932,1050 690,1306 560,1306" fill="var(--grey-soft)"/>
    <polygon points="932,1050 932,1075 750,1306 720,1306" fill="#ffffff"/>
    <polygon points="909,1106 932,1128 932,1306 884,1306 799,1218" fill="var(--blue)"/>

    <!-- centre gold diamond -->
    <polygon points="564,1043 716,1195 600,1306 528,1306 412,1195" fill="url(#goldDiamond)"/>
    <polygon points="564,1090 670,1195 564,1301 458,1195" fill="var(--grey-photo)" role="img" aria-label="Black and white portrait of Owen Halvorsen"/>
  </svg>

  <div class="column-shade"></div>

  <!-- left column -->
  <div class="tag" style="top:44px;width:226px">The Mission:</div>
  <p class="body-text" style="top:98px">To create a family business by purchasing<br>Multifamily Residences, one at a time.</p>

  <div class="tag" style="top:171px;width:171px">Values:</div>
  <p class="body-text" style="top:226px;left:36px">To provide a white glove experience to all<br>residences with a clean, safe, and fun environment</p>

  <div class="tag" style="top:301px;width:233px">The Process:</div>
  <p class="body-text" style="top:352px;font-size:17.5px">Buy right, manage right, and finance right.</p>

  <div class="tag" style="top:410px;width:422px">The Market: Colorado Springs</div>
  <ul class="checklist market-list">
    <li>Projected job growth of nearly 50%</li>
    <li>Below average unemployment rates.</li>
    <li>Above-average incomes.</li>
    <li>Solid economy, military, aerospace, electronics industry, and tourism</li>
  </ul>

  <div class="tag" style="top:656px;width:216px">The Target:</div>
  <p class="body-text" style="top:704px">B and C class assets located in Colorado Springs<br>or nearby submarkets.</p>

  <section class="contact">
    <h2 class="contact-title">Contact:</h2>
    <p class="contact-name">Dean &amp; Owen Halvorsen</p>
    <p class="contact-phone">
      <svg width="34" height="46" viewBox="0 0 34 46" aria-hidden="true"><path d="M9 2 L15 12 L10 16 C10 24 14 32 20 36 L25 32 L32 40 L26 45 C12 42 2 24 4 6 Z" fill="var(--blue)"/></svg>
      719-555-0148
    </p>
    <p class="contact-email">
      <svg width="34" height="20" viewBox="0 0 34 20" aria-hidden="true"><rect x="0" y="0" width="34" height="20" fill="var(--blue)"/><path d="M1 1 L17 12 L33 1" stroke="#fff" stroke-width="2" fill="none"/><path d="M1 19 L13 9 M33 19 L21 9" stroke="#fff" stroke-width="1.5"/></svg>
      dhalvorsen@mailbox.com
    </p>
  </section>

  <!-- right column -->
  <h1 class="team-heading">The Team</h1>
  <div class="tag" style="top:365px;left:486px;width:182px;padding-left:22px">Principals</div>

  <h3 class="principal-name" style="top:428px">Dean Halvorsen</h3>
  <ul class="checklist principal-list" style="top:474px">
    <li>Licensed Colorado Real Estate Agent 18 years.</li>
    <li>Broker-Owner of two HomePoint Realty Franchises 7 and 2 Years.</li>
    <li>Real Estate investing for 5 years.</li>
    <li>Member of Keystone Investors Academy.</li>
    <li>Married 24 years to Marla, parenting 10 children together.</li>
    <li>Appeared on Tom and Lisa's Apartment Hour podcast Episode 43</li>
    <li>$2M portfolio.</li>
  </ul>

  <h3 class="principal-name" style="top:845px">Owen Halvorsen</h3>
  <ul class="checklist principal-list" style="top:891px">
    <li>Retired Electrical Engineer.</li>
    <li>Active Real Estate Investor /Consultant.</li>
    <li>Net worth over $4M</li>
    <li>15 Grandchildren</li>
  </ul>
</main>
</body>
</html>
```